Business Card for a Creative Technology based HR services company

Our company name is Leaf8, and we build large communities of HR (human resource) and finance personnels through our mobile platform, and we conduct lots of on-line and off-line activities to get everyone constantly connected. Behind all these, we will also provide on-site HR and finance contractors to our clients, plus a host of other HR-related services. No process in our company takes more than 5-steps.
Our company slogan: Shaping What Comes Next
Target Market(s)
All human resource (HR) and finance personnels, from new entrants to highly experienced senior professionals.
Industry/Entity Type
Finance
Colors
Designer to choose colors to be used in the design.
Look and feel
Each slider illustrates characteristics of the customer's brand and the style your logo design should communicate.

```html
<!DOCTYPE html>
<html lang="en">
<head>
<meta charset="utf-8">
<title>Leaf8 Business Card</title>
<link href="https://fonts.googleapis.com/css2?family=Open+Sans:wght@300;400;600&display=swap" rel="stylesheet">
<style>
  :root {
    --brand-red: #e8232b;
    --brand-navy: #1c2d50;
    --paper: #ffffff;
    --paper-shade: #f3f3f3;
    --backdrop: #2a2a2c;
    --text-font: "Open Sans", Arial, sans-serif;
  }
  * { margin: 0; padding: 0; box-sizing: border-box; }
  html, body {
    width: 1200px; height: 900px; overflow: hidden;
    background: var(--backdrop);
    font-family: var(--text-font);
  }
  .canvas { position: relative; width: 1200px; height: 900px; }
  .card {
    position: absolute; width: 520px; height: 300px;
    border-radius: 26px; overflow: hidden;
    box-shadow: 0 14px 30px rgba(0,0,0,0.45);
  }
  .card-shape { position: absolute; inset: 0; width: 100%; height: 100%; }

  /* Front */
  .card-front { left: 580px; top: 100px; background: var(--paper); }
  .front-name {
    position: absolute; left: 36px; top: 120px;
    font-weight: 600; font-size: 44px; line-height: 1;
    color: var(--brand-navy);
  }
  .holder { position: absolute; left: 290px; top: 40px; }
  .holder-name { font-weight: 300; font-size: 26px; color: var(--brand-red); line-height: 1.1; }
  .holder-title { font-size: 11px; color: var(--brand-navy); margin-top: 4px; }
  .contact, .address {
    position: absolute; color: var(--paper);
    font-size: 11.5px; line-height: 1.5;
  }
  .contact { left: 30px; bottom: 26px; }
  .address { right: 28px; bottom: 74px; }

  /* Back */
  .card-back { left: 120px; top: 480px; background: var(--brand-navy); }
  .tagline {
    position: absolute; left: 0; right: 0; top: 24px;
    text-align: center;
    color: var(--paper); font-size: 17px; font-weight: 400;
  }
  .back-name {
    position: absolute; left: 0; right: 0; top: 132px;
    text-align: center;
    font-weight: 600; font-size: 64px; line-height: 1;
    color: var(--paper);
  }
</style>
</head>
<body>
<main class="canvas">

  <section class="card card-front" aria-label="Business card front">
    <svg class="card-shape" viewBox="0 0 520 300" preserveAspectRatio="none" aria-hidden="true">
      <rect width="520" height="300" fill="var(--paper-shade)"/>
      <path d="M0,200 L520,120 L520,300 L0,300 Z" fill="var(--brand-red)"/>
    </svg>
    <div class="front-name">Leaf8</div>
    <div class="holder">
      <div class="holder-name">Maya Lorne</div>
      <div class="holder-title">Your Title</div>
    </div>
    <div class="address">
      LEAF8 PTY LTD<br>
      Level 4, 88 Harbour Lane<br>
      Carlton, VIC 3053 Australia
    </div>
    <div class="contact">
      tel: 1300 555 0182 / fax: 61 0 555 0199<br>
      email: info@leaf8studio.com<br>
      www.leaf8studio.com
    </div>
  </section>

  <section class="card card-back" aria-label="Business card back">
    <svg class="card-shape" viewBox="0 0 520 300" preserveAspectRatio="none" aria-hidden="true">
      <rect width="520" height="300" fill="var(--brand-navy)"/>
      <rect width="520" height="72" fill="var(--brand-red)"/>
    </svg>
    <div class="tagline">“Shaping What Comes Next”</div>
    <div class="back-name">Leaf8</div>
  </section>

</main>
</body>
</html>
```